Tallowgate Tailwind Shuttle Co needs a website

We need a logo and website built for our little business. We transport Stand Up Paddle Boarders and Ocean Ski Paddlers from Byron Bay along the coast to places like Ocean Shores, Lennox Head, Ballina where they get out of the bus, hit the ocean and paddle back with the wind to Byron Bay. The website would need a link to a book now button, with a page that allows for the Byron Bay weather,wind forecast on it. Also a side bar that links to our Friendwall page. We would like a weekly schedule of bus times on the website as well,

For themes I really like a ocean based hawaii styled theme if possible. Something that portrays the lifestyle and enjoyment people can have in the ocean. Perhaps a banner image that scrolls where we could also add photos as well over time of the business
Updates

Hi Designers have made the payment non refundable so someone will definitely be getting paid

cheers

Industry/Entity Type

Business

Colors
86acd3
3377b5
35a7d7
0392ce
ffffff
faee3f

Requirements
Nice to have
• Good Imagery of Byron Bay and coastline, I will provide some
A nice logo for the site
Link to a bus timetable where the client can book now, ( i use Quolvo bookings software so can get it to link to the site

```html
<!DOCTYPE html>
<html lang="en">
<head>
<meta charset="utf-8">
<title>Tallowgate Tailwind Shuttle Co</title>
<link href="https://fonts.googleapis.com/css2?family=Source+Sans+3:wght@400;600;700;900&display=swap" rel="stylesheet">
<style>
:root{
  --navy:#0b3566;
  --nav:#2b4f96;
  --royal:#2f5aa8;
  --sky:#35a7d7;
  --ocean:#0392ce;
  --pale:#86acd3;
  --sun:#faee3f;
  --badge:#1ad0f0;
  --ink:#222;
  --link:#1d62b0;
  --white:#ffffff;
  --panel-line:#d6d6d6;
}
*{margin:0;padding:0;box-sizing:border-box}
html,body{width:1200px;height:1054px;overflow:hidden}
body{font-family:"Source Sans 3",sans-serif;color:var(--ink);background:var(--white);position:relative}
.backdrop{position:absolute;left:0;top:43px;width:1200px;height:560px;
  background:linear-gradient(180deg,#2a86d6 0%,#5fb4ea 25%,#3a8ed0 45%,#2d7fc4 55%,#a9d3ee 75%,#ffffff 100%)}
.topnav{position:absolute;left:0;top:0;width:1200px;height:43px;background:linear-gradient(#3a5fa6,#274a8f);box-shadow:0 2px 3px rgba(0,0,0,.35)}
.topnav ul{list-style:none;display:flex;margin-left:141px}
.topnav li{color:var(--white);font-size:12.5px;line-height:43px;padding:0 19px;border-right:1px solid rgba(255,255,255,.12)}
.topnav li:first-child{padding-left:0}
.topnav li:last-child{border:none}
.brand{position:absolute;left:141px;top:58px;display:flex;align-items:center;gap:8px}
.brand .dot{width:22px;height:22px;border-radius:50%;background:var(--navy)}
.brand span{font-size:40px;font-weight:900;color:var(--navy);letter-spacing:-1px}
.partner{position:absolute;left:621px;top:55px;display:flex;align-items:center;gap:14px}
.partner .dot{width:55px;height:55px;border-radius:50%;background:var(--white)}
.partner span{font-size:48px;font-weight:700;color:var(--white)}
.book-now{position:absolute;left:867px;top:64px;width:192px;height:50px;border:2px solid var(--white);border-radius:8px;
  background:linear-gradient(#4d9bf0,#1e64d0);color:var(--white);font-size:30px;text-align:center;line-height:44px}
.hero{position:absolute;left:141px;top:134px;width:918px;height:319px;border:1px solid #cfe6f7;
  background:linear-gradient(180deg,#8fc6ee 0%,#cfe6f5 45%,#4bb7d8 62%,#1f9ec4 100%);box-shadow:0 8px 8px -4px rgba(0,0,0,.4)}
.search{position:absolute;left:29px;top:20px;width:333px;height:276px;background:rgba(30,80,150,.28);padding:16px 20px}
.search h2{color:var(--white);font-weight:400;font-size:22px;margin-bottom:12px}
.search .field{display:flex;align-items:center;gap:6px;margin-bottom:18px}
.search .input{width:245px;height:22px;background:var(--white);border:1px solid #ccc;border-radius:2px;font-size:12px;color:#777;padding-left:8px;line-height:20px}
.search .btn{margin-top:20px;width:243px;height:40px;border-radius:20px;background:linear-gradient(#3d64ad,#22458e);color:var(--white);font-size:20px;text-align:center;line-height:40px;margin-left:3px}
.card{position:absolute;top:500px;width:289px;height:215px;background:linear-gradient(#fff,#f2f2f2);border:1px solid #e0e0e0;box-shadow:0 0 4px rgba(0,0,0,.08)}
.card h3{font-weight:400;font-size:14.5px;color:var(--navy);position:absolute;left:16px;top:14px}
.weather{left:141px}
.sun{position:absolute;left:12px;top:64px;width:80px;height:80px;border-radius:50%;background:radial-gradient(circle,#ffe55a 30%,#f7c600 55%,rgba(255,220,80,0) 70%)}
.temps{position:absolute;left:116px;top:84px;font-size:20px;line-height:25px;color:#111}
.wind{left:455px}
.wind .date{position:absolute;left:17px;top:36px;width:261px;height:35px;border:1px solid #bbb;background:#f7f7f7;font-size:12.5px;color:#444;padding:10px 12px}
.rows{position:absolute;left:17px;top:76px;width:261px}
.row{display:flex;align-items:center;height:44px;font-size:9px;color:#333}
.hour{width:30px;height:42px;color:var(--white);font-weight:700;font-size:14px;line-height:42px;padding-left:2px;background:linear-gradient(90deg,#16d3a6,#2ac6f0)}
.spd{width:50px;font-size:15px;font-weight:700;text-align:center;line-height:12px}
.spd small{display:block;font-size:6px;font-weight:400}
.tmp{width:56px;text-align:center;font-size:6px;line-height:9px}
.tmp b{display:inline-block;background:#fff200;font-size:12px;padding:0 6px;border-radius:3px;line-height:15px}
.sky{width:40px;text-align:center;font-size:7px}
.wave{width:40px;text-align:center;font-size:6px;line-height:9px}
.wave b{display:inline-block;background:var(--badge);font-size:12px;padding:0 3px;border-radius:3px;line-height:15px;color:#083060}
.times{left:770px}
.times svg.cal{position:absolute;right:16px;top:18px}
.times table{position:absolute;left:15px;top:45px;width:259px;border-collapse:collapse;font-size:12.5px}
.times td{border:1px solid #bdbdbd;height:28px;padding:4px 8px 0;vertical-align:middle}
.times td+td{text-align:center;color:#333}
.times tr:first-child td+td{color:var(--navy)}
.welcome{position:absolute;left:142px;top:731px;width:920px;font-size:12.2px;line-height:19px}
.welcome h3{font-weight:400;font-size:14.5px;color:var(--navy);margin-bottom:7px}
.welcome p{margin-bottom:19px}
.welcome a{color:var(--link);text-decoration:none;position:relative;top:-14px}
.footer{position:absolute;left:0;top:892px;width:1200px;height:120px;background:var(--navy);color:var(--white)}
.footer h4{text-align:center;font-weight:400;font-size:16px;padding-top:16px;padding-bottom:12px;border-bottom:1px solid #2a5185;width:918px;margin-left:141px}
.footer .contact{position:absolute;top:34px;font-size:14.5px;line-height:60px}
.legal{position:absolute;top:1026px;width:1200px;text-align:center;font-size:12.5px;color:#444}
.side-tab{position:absolute;left:0;top:423px;width:36px;height:95px;background:var(--nav);border:1px solid #9fb6dc;display:flex;align-items:center;justify-content:center}
.side-tab span{transform:rotate(-90deg);color:var(--white);font-weight:700;font-size:14px;white-space:nowrap}
</style>
</head>
<body>
<div class="backdrop" role="img" aria-label="Bright tropical sky and ocean surf background"></div>

<nav class="topnav"><ul>
  <li>HOME</li><li>ABOUT US</li><li>BOOK TICKET</li><li>CANCEL TICKET</li><li>CONTACT US</li>
</ul></nav>

<div class="brand"><div class="dot"></div><span>Tallowgate Tailwind</span></div>
<div class="partner"><div class="dot"></div><span>Quolvo</span></div>
<div class="book-now">Book Now</div>

<section class="hero" role="img" aria-label="Stand up paddle boarder on a tropical sea near a palm island">
  <div class="search">
    <h2>Find your Tickets</h2>
    <div class="field"><div class="input">From</div></div>
    <div class="field"><div class="input">To</div></div>
    <div class="field"><div class="input">When</div>
      <svg width="14" height="14" viewBox="0 0 14 14"><rect x="1" y="2" width="12" height="11" fill="#fff" stroke="#f08a1c" stroke-width="1.5"/><rect x="1" y="2" width="12" height="3" fill="#f08a1c"/><path d="M4 7h2v2H4zM8 7h2v2H8zM4 10h2v2H4zM8 10h2v2H8z" fill="#f08a1c"/></svg>
    </div>
    <div class="btn">Search Tickets</div>
  </div>
</section>

<section class="card weather">
  <h3>Weather Report</h3>
  <div class="sun"></div>
  <div class="temps">31°C°F<br>H32° L22°</div>
</section>

<section class="card wind">
  <h3>Wind forecast</h3>
  <div class="date">Monday, December 30, 2013</div>
  <div class="rows">
    <div class="row"><div class="hour">01h</div>
      <svg width="26" height="26" viewBox="0 0 26 26"><path d="M2 2 L24 22 L14 21 L18 17Z" fill="#111"/></svg>
      <div class="spd">16 <sup style="font-size:7px">kts</sup><small>max 16 kts</small></div>
      <div class="tmp"><b>12°C</b><br>1004 hPa</div>
      <div class="sky"><svg width="18" height="18" viewBox="0 0 18 18"><path d="M11 2a7 7 0 1 0 5 12A8 8 0 0 1 11 2z" fill="#f2c94c"/></svg><br>0 mm</div>
      <svg width="26" height="16" viewBox="0 0 26 16"><path d="M1 2 L24 12 L12 14 L15 9Z" fill="#111"/></svg>
      <div class="wave"><b>0.8m</b><br>5 s</div></div>
    <div class="row"><div class="hour">04h</div>
      <svg width="26" height="26" viewBox="0 0 26 26"><path d="M2 2 L24 22 L14 21 L18 17Z" fill="#111"/></svg>
      <div class="spd">12 <sup style="font-size:7px">kts</sup><small>max 12 kts</small></div>
      <div class="tmp"><b>12°C</b><br>1003 hPa</div>
      <div class="sky"><svg width="18" height="18" viewBox="0 0 18 18"><path d="M11 2a7 7 0 1 0 5 12A8 8 0 0 1 11 2z" fill="#f2c94c"/></svg><br>0 mm</div>
      <svg width="26" height="16" viewBox="0 0 26 16"><path d="M1 2 L24 12 L12 14 L15 9Z" fill="#111"/></svg>
      <div class="wave"><b>0.7m</b><br>6 s</div></div>
    <div class="row"><div class="hour">07h</div>
      <svg width="26" height="26" viewBox="0 0 26 26"><path d="M2 2 L24 22 L14 21 L18 17Z" fill="#111"/></svg>
      <div class="spd">9 <sup style="font-size:7px">kts</sup><small>max 9 kts</small></div>
      <div class="tmp"><b>12°C</b><br>1003 hPa</div>
      <div class="sky"><svg width="20" height="20" viewBox="0 0 20 20"><circle cx="10" cy="10" r="5" fill="#f7c600"/><g stroke="#f7c600" stroke-width="1.5"><path d="M10 1v3M10 16v3M1 10h3M16 10h3M4 4l2 2M14 14l2 2M4 16l2-2M14 6l2-2"/></g></svg><br>0 mm</div>
      <svg width="26" height="16" viewBox="0 0 26 16"><path d="M1 2 L24 12 L12 14 L15 9Z" fill="#111"/></svg>
      <div class="wave"><b>0.6m</b><br>6 s</div></div>
  </div>
</section>

<section class="card times">
  <h3>Bus Timings</h3>
  <svg class="cal" width="14" height="14" viewBox="0 0 14 14"><rect x="1" y="2" width="12" height="11" fill="#fff" stroke="#f08a1c" stroke-width="1.5"/><rect x="1" y="2" width="12" height="3" fill="#f08a1c"/><path d="M4 7h2v2H4zM8 7h2v2H8zM4 10h2v2H4zM8 10h2v2H8z" fill="#f08a1c"/></svg>
  <table>
    <tr><td>Date</td><td>01.06.2014</td><td>01.08.2014</td></tr>
    <tr><td>Departure TIme</td><td>6.30 pm</td><td>6.30 pm</td></tr>
    <tr><td>Load up at</td><td>6.00 pm</td><td>6.00 pm</td></tr>
    <tr><td>Start</td><td>6.30 pm</td><td>6.30 pm</td></tr>
    <tr><td>Finish</td><td>5.30 am</td><td>5.30 am</td></tr>
    <tr><td>Distance</td><td>600km</td><td>600km</td></tr>
  </table>
</section>

<section class="welcome">
  <h3>Welcome</h3>
  <p>Lorem ipsum dolor sit amet, consectetur adipiscing elit. Vivamus interdum arcu sed vehicula scelerisque. Cras rhoncus, eros nec gravida malesuada, nibh neque porttitor nulla, id volutpat massa ante id &nbsp;ctus.tempus. Fusce in euismod massa.Lorem ipsum dolor sit amet, consectetur adipiscing elit. Vivamus i.</p>
  <p>Lorem ipsum dolor sit amet, consectetur adipiscing elit. Vivamus interdum arcu sed vehicula scelerisque. Cras rhoncus, eros nec gravida malesuada, nibh neque porttitor nulla, id volutpat massa ante id &nbsp;ctus.tempus. Fusce in euismod massa.</p>
  <a href="#">More about us...</a>
</section>

<footer class="footer">
  <h4>GET IN TOUCH</h4>
  <div class="contact" style="left:248px">PH : 0491 570 118</div>
  <div class="contact" style="left:496px">info@tallowgatetailwind.example</div>
  <div class="contact" style="left:845px;font-weight:600;color:#cfd8e6">Friendwall</div>
</footer>
<div class="legal">© 2013 Bus Booking Services. All Rights Reserved</div>

<div class="side-tab"><span>Friendwall</span></div>
</body>
</html>
```